Pell Hamlet Summer Party Invitation

We need an invitation to be designed for our annual summer party for Pell Hamlet in Chelsea, London. The area has a relaxed family atmosphere but is on the edge of the bustle of Chelsea. The committee has specified the following:

TO INCLUDE THE FOLLOWING INFORMATION - will it be the same two sided format as last year? Maybe the reverse can use your pale blue and your London skyline "logo"

Should the following, highlighted in blue, be very bold on the front of the invite? With the Dorrow & Co sales and lettings logo.
SUMMER PARTY 2016
Pell Hamlet Chelsea is holding a Summer Party to celebrate the Queen's 90th Birthday

Date: Saturday 18th June 2016
Time: 2.00pm to 5.00pm
Place: Wimbrel Lane South (the pedestrianised section off Hassock Street) MAP?

Open to all residents of Pell Hamlet and admittance is by invitation only.
Please keep this invitation safe and bring it with you on the day

Then more detail on the rear:

Pell Hamlet Chelsea
Formerly known as Falbrook Residents' Association of Pell Hamlet

Email: falbrookra@mailvane.co.uk
Website: falbrookra-demo.co.uk
OUR TYPEFACE IS ARIAL. The rest can be in any typeface but Arial is our "logo"

Dress code: red white and blue (or black ) as simple or elaborate as you like Live Music Children's entertainment and activities Food Drinks Tea and cakes

SPONSORS:
Dorrow & Co. Ensuring this is prominent as the main sponsor Gilded Otter
412 Blues club etc etc
Harrow Pike Studios
List to follow.............

Space needs to be left on the rear for sponsors details to be added. They would like something with an almost retro, traditional British feel.
Our Dorrow & Co logo attached and branding.

Also a flyer that association seemed to like.

I would suggest postcard (A6 sized) or maybe A5 at the biggest

Target Market(s)

Local Residents

Colors
ec1f27
ffffff
0355a3

Requirements
Must have
• Information on the description

```html
<!DOCTYPE html>
<html lang="en">
<head>
<meta charset="utf-8">
<title>Pell Hamlet Summer Party 2016 – Invitation</title>
<link rel="stylesheet" href="https://fonts.googleapis.com/css2?family=Archivo:ital,wght@0,400;0,600;0,700;0,800;1,500;1,600;1,700&family=Bebas+Neue&display=swap">
<style>
  :root {
    --stage: #1380bf;
    --navy: #0c2a5b;
    --frame-navy: #062a57;
    --flag-navy: #0a3466;
    --flag-red: #d41f2b;
    --white: #ffffff;
    --teal: #0f6f8c;
    --teal-light: #2a8ca8;
    --brand-teal: #1a8fb0;
    --emblem: #7a3c7d;
    --red-text: #d41f2b;
  }
  * { margin: 0; padding: 0; box-sizing: border-box; }
  html, body { width: 1200px; height: 1000px; overflow: hidden; }
  body {
    background: var(--stage);
    position: relative;
    font-family: "Archivo", Arial, sans-serif;
    color: var(--navy);
  }
  .invite {
    position: absolute;
    top: 160px;
    width: 483px;
    height: 680px;
  }
  .invite--front { left: 95px; }
  .invite--back { left: 623px; }
  .invite__flag { position: absolute; inset: 0; width: 483px; height: 680px; display: block; }
  .invite__panel {
    position: absolute;
    left: 35px; top: 35px;
    width: 413px; height: 610px;
    background: var(--white);
    overflow: hidden;
  }
  .skyline {
    position: absolute;
    left: 0; top: 510px;
    width: 100%; height: 45px;
    background: linear-gradient(180deg, rgba(15,111,140,0) 0%, rgba(42,140,168,0.55) 45%, var(--teal) 100%);
  }
  .contact-band {
    position: absolute;
    left: 0; top: 555px;
    width: 100%; height: 55px;
    background: var(--teal);
    color: var(--white);
    text-align: center;
    font-weight: 700;
    font-size: 15px;
    line-height: 18px;
    padding-top: 2px;
  }
  .centered { position: absolute; left: 0; width: 100%; text-align: center; }
  .title {
    top: 17px;
    font-family: "Bebas Neue", "Oswald", sans-serif;
    font-size: 58px;
    line-height: 56px;
    color: var(--navy);
    letter-spacing: 0.5px;
  }
  .sponsor-brand {
    position: absolute;
    right: 48px; top: 68px;
    font-weight: 800;
    font-size: 15px;
    color: var(--brand-teal);
  }
  .emblem {
    position: absolute;
    left: 163px; top: 97px;
    width: 87px; height: 108px;
    border-radius: 44px 44px 10px 10px;
    background: linear-gradient(180deg, #8a4a8d 0%, #c7a7c6 100%);
  }
  .details {
    top: 218px;
    font-size: 13px;
    line-height: 16px;
    font-weight: 700;
  }
  .details p + p { margin-top: 16px; }
  .details .italic { font-style: italic; }
  .details .note { font-style: italic; font-weight: 600; }
  .place { top: 433px; font-weight: 700; font-size: 15px; line-height: 19px; }

  .assoc { top: 17px; }
  .assoc__name { font-size: 19px; font-weight: 800; line-height: 22px; }
  .assoc__former { font-size: 14px; font-style: italic; font-weight: 500; line-height: 19px; }
  .dress { top: 108px; font-size: 14px; font-weight: 700; line-height: 18.5px; }
  .refreshments { top: 197px; font-size: 19px; font-weight: 800; line-height: 24px; color: var(--red-text); }
  .refreshments .bullet { color: var(--navy); }
  .sponsors { top: 256px; }
  .sponsors__heading { font-size: 17px; font-weight: 800; line-height: 20px; letter-spacing: 0.3px; }
  .sponsors__list { font-size: 14px; font-style: italic; font-weight: 600; line-height: 19px; }
</style>
</head>
<body>

<svg width="0" height="0" style="position:absolute">
  <defs>
    <g id="union-border">
      <rect width="483" height="680" fill="var(--flag-navy)"/>
      <g stroke="var(--white)" stroke-width="70">
        <line x1="0" y1="0" x2="483" y2="680"/>
        <line x1="483" y1="0" x2="0" y2="680"/>
      </g>
      <g stroke="var(--flag-red)" stroke-width="22">
        <line x1="0" y1="0" x2="483" y2="680"/>
        <line x1="483" y1="0" x2="0" y2="680"/>
      </g>
      <rect x="160" y="0" width="162" height="680" fill="var(--white)"/>
      <rect x="0" y="283" width="483" height="113" fill="var(--white)"/>
      <rect x="193" y="0" width="97" height="680" fill="var(--flag-red)"/>
      <rect x="0" y="305" width="483" height="67" fill="var(--flag-red)"/>
      <rect x="23" y="23" width="437" height="634" fill="var(--frame-navy)"/>
    </g>
  </defs>
</svg>

<section class="invite invite--front">
  <svg class="invite__flag" viewBox="0 0 483 680" aria-hidden="true"><use href="#union-border"/></svg>
  <div class="invite__panel">
    <h1 class="centered title">SUMMER PARTY 2016</h1>
    <div class="sponsor-brand">Dorrow &amp; Co</div>
    <div class="emblem" role="img" aria-label="Queen's 90th birthday celebration badge"></div>
    <div class="centered details">
      <p>SUMMER PARTY 2016<br>Pell Hamlet Chelsea is holding<br>a Summer Party to celebrate<br>the Queen's 90th Birthday</p>
      <p class="italic">Date: Saturday 18th June 2016<br>Time: 2.00pm to 5.00pm</p>
      <p class="note">* Open to all residents of Pell Hamlet<br>admittance is by invitation only</p>
      <p class="note">* Please keep this invitation safe<br>and bring it with you on the day</p>
    </div>
    <div class="centered place">
      Place:<br>Wimbrel Lane South<br>(the pedestrianised section off Hassock Street)
    </div>
    <div class="skyline" role="img" aria-label="London skyline silhouette"></div>
    <div class="contact-band">
      Email: falbrookra@mailvane.co.uk<br>Website: www.falbrookra-demo.co.uk
    </div>
  </div>
</section>

<section class="invite invite--back">
  <svg class="invite__flag" viewBox="0 0 483 680" aria-hidden="true"><use href="#union-border"/></svg>
  <div class="invite__panel">
    <div class="centered assoc">
      <h2 class="assoc__name">Pell Hamlet Chelsea</h2>
      <p class="assoc__former">Formerly known as<br>Falbrook Residents' Association of Pell Hamlet</p>
    </div>
    <p class="centered dress">
      Dress code: red white and blue (or black)<br>as simple or elaborate as you like<br>Live Music Children's entertainment and activities
    </p>
    <p class="centered refreshments">
      <span class="bullet">•</span> Food <span class="bullet">•</span> Drinks <span class="bullet">•</span> Tea <span class="bullet">•</span> Cakes
    </p>
    <div class="centered sponsors">
      <h3 class="sponsors__heading">SPONSORS:</h3>
      <p class="sponsors__list">Dorrow &amp; Co, 412 Blues Club, Harrow Pike Studios</p>
    </div>
    <div class="skyline" role="img" aria-label="London skyline silhouette"></div>
    <div class="contact-band">
      Email: falbrookra@mailvane.co.uk<br>Website: www.falbrookra-demo.co.uk
    </div>
  </div>
</section>

</body>
</html>
```